Garage Door Sales and Repair Website

Looking for a website theme and home page design for a garage door sales and repair company (Cedar Ridge Overhead).   We have a new logo and color scheme (attached) and need to update our website to match.  Here is the current site http://www.cedarridgeoverhead.example/
The design should lend it self to being responsive and full screen.
I like this site (http://www.brightpane-studio.example/) how it has different color blocks and I would like to have a slide show on my home page as well.  4 slides utilizing some of the following concepts Garage Opener, Garage Doors, Springs, Garage Door Repair, Specials, Free Estimate, etc...
Would like color design to match logo / business cards attached.
Call for Free Estimate with phone number should be visible on top of the page as well.

Consumers
Professional Service
1 page
Other font styles liked:
- Oswald, Open Sans, other similar google web fonts

Requirements
Must have
- 4 slides for home page design
- Free Estimate
- Phone Number

Nice to have
- Call out for online specials

```html
<!DOCTYPE html>
<html lang="en">
<head>
<meta charset="utf-8">
<title>Cedar Ridge Overhead — Garage Door Sales and Repair</title>
<link rel="stylesheet" href="https://fonts.googleapis.com/css2?family=Oswald:wght@400;500&family=Roboto:wght@400;500&display=swap">
<style>
:root{
  --navy:#4b5479;
  --navy-dark:#3f476a;
  --slate:#6a7398;
  --btn-top:#636c95;
  --btn-bottom:#444c72;
  --ink:#2b2b2b;
  --body:#555;
  --soft:#f1f1f1;
  --white:#fff;
  --black:#151515;
}
*{margin:0;padding:0;box-sizing:border-box}
html,body{width:1200px;height:2442px;overflow:hidden}
body{position:relative;font-family:"Roboto",Arial,sans-serif;color:var(--ink);background:var(--white)}
.abs{position:absolute}

.topbar{left:0;top:0;width:1200px;height:36px;background:var(--navy);color:var(--white);font-size:12px}
.topbar .mail{left:93px;top:11px;display:flex;align-items:center;gap:7px}
.topbar .estimate{left:809px;top:0;width:196px;height:36px;background:var(--navy-dark);display:flex;align-items:center;justify-content:center;font-size:12px;letter-spacing:.3px}
.topbar .phone{left:1015px;top:11px;display:flex;align-items:center;gap:7px}

.nav{left:0;top:36px;width:1200px;height:102px;background:var(--white)}
.nav a{position:absolute;top:46px;font-size:16px;letter-spacing:.5px;color:#333;text-decoration:none}
.nav a.active{color:var(--navy)}
.brand{left:526px;top:40px;width:148px;height:148px;border-radius:50%;background:var(--white);z-index:3;display:flex;align-items:center;justify-content:center;text-align:center;font-family:"Oswald",sans-serif;font-weight:500;font-size:21px;line-height:1.1;color:var(--navy);padding:0 18px}

.hero{left:0;top:138px;width:1200px;height:542px;background:linear-gradient(180deg,#3c4a3a 0%,#6d6a5e 45%,#8c7c66 75%,#4d4436 100%)}
.hero h1{position:absolute;left:93px;top:234px;font-family:"Oswald",sans-serif;font-weight:400;color:var(--white);text-transform:uppercase;line-height:1.12}
.hero h1 .l1{display:block;font-size:44px}
.hero h1 .l2{display:block;font-size:38px}
.hero h1 .l3{display:block;font-size:56px;font-weight:500}
.hero .arrows{position:absolute;left:1068px;top:478px;display:flex;gap:12px}

.about{left:0;top:680px;width:1200px;height:237px;background:var(--soft);text-align:center}
.section-title{font-family:"Roboto",sans-serif;font-weight:400;font-size:28px;letter-spacing:.5px;color:var(--ink)}
.section-title span{color:var(--navy)}
.about .section-title{margin-top:30px}
.about p{width:920px;margin:14px auto 0;font-size:14px;line-height:24px;color:var(--body)}
.btn{display:inline-flex;align-items:center;justify-content:center;background:linear-gradient(var(--btn-top),var(--btn-bottom));color:var(--white);font-size:15px;border-radius:3px}
.about .btn{position:absolute;left:474px;top:167px;width:252px;height:45px}

.services-title{left:0;top:950px;width:1200px;text-align:center}
.card{top:1024px;width:249px;height:252px;background:var(--white);box-shadow:0 2px 5px rgba(0,0,0,.25);text-align:center}
.card .photo{width:249px;height:160px}
.card h3{font-weight:400;font-size:15px;margin-top:20px;color:var(--ink)}
.card .pill{display:inline-flex;align-items:center;justify-content:center;margin-top:11px;width:92px;height:28px;border-radius:14px;background:linear-gradient(var(--btn-top),var(--btn-bottom));color:var(--white);font-size:10px}

.specials{left:0;top:1322px;width:1200px;height:343px;background:var(--slate);color:var(--white);text-align:center}
.specials h2{font-weight:400;font-size:33px;margin-top:52px}
.specials h3{font-weight:400;font-size:27px;margin-top:18px}
.specials p{font-size:19px;line-height:31px;margin-top:10px}
.specials .outline{position:absolute;left:529px;top:244px;width:140px;height:46px;border:1px solid #e4e6ee;border-radius:3px;display:flex;align-items:center;justify-content:center;font-size:18px}

.blog-title{left:0;top:1708px;width:1200px;text-align:center}
.post{top:1778px;width:316px}
.post .photo{width:316px;height:192px;border:2px solid #e2e2e2}
.post h4{font-weight:400;font-size:16px;margin-top:14px;color:#333}
.post p{font-size:11.5px;line-height:18px;margin-top:8px;color:#555}
.post .more{font-size:12px;margin-top:10px;color:#444;display:flex;align-items:center;gap:3px}

.footer{left:0;top:2125px;width:1200px;height:219px;background:var(--navy);color:var(--white)}
.footer .badge{left:88px;top:66px;width:172px;text-align:center;font-family:"Oswald",sans-serif;font-weight:400;font-size:16px;line-height:1.25}
.footer .badge .name{font-size:19px}
.footer .badge .num{font-size:30px}
.footer h5{font-weight:500;font-size:13px;letter-spacing:.3px}
.footer .col{top:53px;font-size:12px}
.newsletter{left:358px;width:240px}
.newsletter p{margin-top:14px;line-height:16px}
.newsletter .field{margin-top:14px;width:215px;height:31px;background:#f3f3f3;color:#777;font-size:11px;padding:9px 10px}
.newsletter .sub{margin-top:14px;width:96px;height:26px;background:#2b2f3b;display:flex;align-items:center;justify-content:center;font-size:11px}
.contact{left:690px}
.contact ul{list-style:none;margin-top:16px;line-height:24.5px}
.social{left:960px}
.social ul{list-style:none;margin-top:14px}
.social li{display:flex;align-items:center;gap:18px;height:43px}
.social .dot{width:34px;height:34px;border-radius:50%;border:1px solid #c9cde0}

.bottom{left:0;top:2344px;width:1200px;height:98px;background:var(--black);color:var(--white);font-size:12px;display:flex;align-items:center;justify-content:center}
</style>
</head>
<body>

<header class="abs topbar">
  <div class="abs mail">
    <svg width="12" height="9" viewBox="0 0 12 9"><rect x="0.5" y="0.5" width="11" height="8" fill="none" stroke="#fff"/><path d="M0.5 0.5 6 5 11.5 0.5" fill="none" stroke="#fff"/></svg>
    info@cedarridgeoverhead.example
  </div>
  <div class="abs estimate">CALL FOR FREE ESTIMATE</div>
  <div class="abs phone">
    <svg width="12" height="12" viewBox="0 0 24 24"><path fill="#fff" d="M6.6 10.8a15 15 0 0 0 6.6 6.6l2.2-2.2c.3-.3.7-.4 1-.2 1.1.4 2.3.6 3.6.6.6 0 1 .4 1 1V20c0 .6-.4 1-1 1A17 17 0 0 1 3 4c0-.6.4-1 1-1h3.5c.6 0 1 .4 1 1 0 1.3.2 2.5.6 3.6.1.3 0 .7-.2 1z"/></svg>
    303-555-0147
  </div>
</header>

<nav class="abs nav">
  <a class="active" style="left:89px">HOME</a>
  <a style="left:206px">OPENERS</a>
  <a style="left:351px">BROKEN SPRINGS</a>
  <a style="left:713px">GARAGE DOORS</a>
  <a style="left:916px">GARAGE DOOR REPAIR</a>
</nav>
<div class="abs brand">Cedar Ridge Overhead</div>

<section class="abs hero" role="img" aria-label="Slide photo of a two-storey house at dusk with lit windows and white carriage-style garage doors">
  <h1><span class="l1">Denver’s Preferred</span><span class="l2">Garage Door Sales and</span><span class="l3">Repair Company</span></h1>
  <div class="arrows">
    <svg width="14" height="22" viewBox="0 0 14 22"><path d="M11 2 3 11l8 9" fill="none" stroke="#fff" stroke-width="2"/></svg>
    <svg width="14" height="22" viewBox="0 0 14 22"><path d="M3 2l8 9-8 9" fill="none" stroke="#fff" stroke-width="2"/></svg>
  </div>
</section>

<section class="abs about">
  <h2 class="section-title">ABOUT <span>US</span></h2>
  <p>Garage door openers not only provide convenience for the homeowner. They also provide security. The garage door is the largest door or entryway into your home, and as such, needs to be kept secure at all times. A high quality, expertly installed garage door opener is the best way to safeguard your home, and give you and your family the peace of mind you deserve!</p>
  <span class="btn">SCHEDULE FREE ESTIMATE</span>
</section>

<h2 class="abs section-title services-title">OUR <span>SERVICES</span></h2>

<article class="abs card" style="left:86px">
  <div class="photo" role="img" aria-label="Technician in a cap repairing a garage door" style="background:linear-gradient(135deg,#5a3a26,#8b5a3a 55%,#2f2a28)"></div>
  <h3>GARAGE DOOR REPAIR</h3><span class="pill">MORE INFO</span>
</article>
<article class="abs card" style="left:346px">
  <div class="photo" role="img" aria-label="Red and white garage door opener motor unit" style="background:linear-gradient(135deg,#f4f4f4,#dcdcdc 60%,#b3212a)"></div>
  <h3>GARAGE DOOR OPENERS</h3><span class="pill">MORE INFO</span>
</article>
<article class="abs card" style="left:604px">
  <div class="photo" role="img" aria-label="House front with two beige panelled garage doors" style="background:linear-gradient(180deg,#6d6a5e,#9a9584 55%,#7b7666)"></div>
  <h3>NEW GARAGE DOORS</h3><span class="pill">MORE INFO</span>
</article>
<article class="abs card" style="left:863px">
  <div class="photo" role="img" aria-label="Close-up of garage door torsion springs" style="background:linear-gradient(180deg,#3b3530,#8a6a4e 55%,#4a4038)"></div>
  <h3>BROKEN SPRINGS</h3><span class="pill">MORE INFO</span>
</article>

<section class="abs specials" role="region" aria-label="Specials">
  <h2>SPECIALS</h2>
  <h3>SAME DAY GARAGE DOOR REPAIR &amp; SERVICE</h3>
  <p>Fast — Affordable — Professional — No Additional Charge For Weekends<br>– 24 Hour Emergency Service Available</p>
  <span class="outline">VIEW OFFER</span>
</section>

<h2 class="abs section-title blog-title">LATEST <span>BLOG</span></h2>

<article class="abs post" style="left:85px">
  <div class="photo" role="img" aria-label="Modern frosted glass garage doors on a wood-clad house" style="background:linear-gradient(135deg,#5b3b2a,#c9c3bc 50%,#3a3430)"></div>
  <h4>Neque porro quisquam est</h4>
  <p>Lorem ipsum dolor sit amet, consectetur adipiscing elit. Sed blandit massa vel mauris sollicitudin dignissim. Lorem ipsum</p>
  <span class="more">Read More <svg width="8" height="8" viewBox="0 0 8 8"><path d="M1 1l3 3-3 3M4 1l3 3-3 3" fill="none" stroke="#444"/></svg></span>
</article>
<article class="abs post" style="left:436px">
  <div class="photo" role="img" aria-label="Ceiling-mounted garage door opener in a tidy garage" style="background:linear-gradient(180deg,#e9e9e9,#cfcfcf 60%,#9c9c9c)"></div>
  <h4>Neque porro quisquam est</h4>
  <p>Lorem ipsum dolor sit amet, consectetur adipiscing elit. Sed blandit massa vel mauris sollicitudin dignissim. Lorem ipsum</p>
  <span class="more">Read More <svg width="8" height="8" viewBox="0 0 8 8"><path d="M1 1l3 3-3 3M4 1l3 3-3 3" fill="none" stroke="#444"/></svg></span>
</article>
<article class="abs post" style="left:790px">
  <div class="photo" role="img" aria-label="Stone house with two wooden arched garage doors" style="background:linear-gradient(135deg,#b95a3a,#d4cbbd 45%,#9a4a26)"></div>
  <h4>Neque porro quisquam est</h4>
  <p>Lorem ipsum dolor sit amet, consectetur adipiscing elit. Sed blandit massa vel mauris sollicitudin dignissim. Lorem ipsum</p>
  <span class="more">Read More <svg width="8" height="8" viewBox="0 0 8 8"><path d="M1 1l3 3-3 3M4 1l3 3-3 3" fill="none" stroke="#444"/></svg></span>
</article>

<footer class="abs footer">
  <div class="abs badge">
    <div class="name">Cedar Ridge Overhead</div>
    <div>Call for a FREE Estimate</div>
    <div class="num">303-555-0147</div>
  </div>
  <div class="abs col newsletter">
    <h5>NEWSLETTERS SIGN UP</h5>
    <p>Sign up for our daily email by entering your information below</p>
    <div class="field">Email address</div>
    <div class="sub">SUBSCRIBE</div>
  </div>
  <div class="abs col contact">
    <h5>GET IN TOUCH</h5>
    <ul>
      <li>Address : 1450 Larkspur Lane,</li>
      <li>Arvada, CO</li>
      <li>Phone : 720 555 0192</li>
      <li>Email : hello@samplemail.example</li>
    </ul>
  </div>
  <div class="abs col social">
    <h5>FOLLOW US ON</h5>
    <ul>
      <li><span class="dot"></span>Porchboard</li>
      <li><span class="dot"></span>Chirpline</li>
      <li><span class="dot"></span>Snapframe</li>
    </ul>
  </div>
</footer>

<div class="abs bottom">Copyright © 2016 &nbsp;All Rights Reserved</div>

</body>
</html>
```